International Trading Company, 'KIRO' needs a Business Card

The company name is "KIRO" and it has own logo design.
I'd like to use its logo on this business card.
I need two side Business Card.
I'll look forward to your great design.
Thank you very much in advance.

Contact Information for Business Card

Company Name : Kiro Harbour Limited
Information Example
Dorian Pallister
Mobile(use icon please) : 1 (212) 555-0143
Tel(use icon please) : 1 (212) 555-0178
Email(use icon please) : dorian27@kiroharbour-mail.com
Address(use icon please) : 482 Halden Ave, New York, NY 10160, USA

```html
<!DOCTYPE html>
<html lang="en">
<head>
<meta charset="UTF-8">
<title>Kiro Harbour Limited — Business Card</title>
<link rel="stylesheet" href="https://fonts.googleapis.com/css2?family=Montserrat:wght@400;800&family=Open+Sans:wght@400&display=swap">
<style>
  :root {
    --backdrop: #2b2b2b;
    --card: #121212;
    --card-edge: #1c1c1c;
    --logo-gloss: #3a3a3a;
    --logo-back: #7c7c7c;
    --text-name: #9a9a9a;
    --text-muted: #7a7a7a;
    --text-contact: #8c8c8c;
    --icon: #8c8c8c;
  }
  * { margin: 0; padding: 0; box-sizing: border-box; }
  html, body {
    width: 800px; height: 1200px; overflow: hidden;
    background: var(--backdrop);
  }
  .canvas {
    position: relative; width: 800px; height: 1200px;
  }
  .card {
    position: absolute; left: 60px;
    width: 680px; height: 388px;
    background: var(--card);
    border: 1px solid var(--card-edge);
    box-shadow: 0 14px 30px rgba(0,0,0,0.45);
  }
  .card--front { top: 150px; }
  .card--back { top: 662px; }

  .wordmark {
    font-family: "Montserrat", sans-serif;
    font-weight: 800;
    letter-spacing: 4px;
    line-height: 1;
  }
  .card--front .wordmark {
    position: absolute; left: 0; right: 0; top: 150px;
    text-align: center;
    font-size: 92px;
    color: var(--logo-gloss);
  }
  .card--back .wordmark {
    position: absolute; right: 56px; top: 150px;
    font-size: 56px;
    color: var(--logo-back);
  }

  .holder {
    position: absolute; left: 50px; top: 44px;
    font-family: "Open Sans", sans-serif;
  }
  .holder__name { font-size: 20px; color: var(--text-name); }
  .holder__role { font-size: 11px; color: var(--text-muted); margin-top: 4px; }

  .contacts {
    position: absolute; left: 50px; top: 222px;
    list-style: none;
    font-family: "Open Sans", sans-serif;
    font-size: 12px; color: var(--text-contact);
  }
  .contacts li {
    display: flex; align-items: center;
    height: 24px;
  }
  .contacts svg {
    width: 12px; height: 12px; margin-right: 12px;
    fill: none; stroke: var(--icon); stroke-width: 1.6;
  }
</style>
</head>
<body>
<main class="canvas">
  <section class="card card--front" aria-label="Card front">
    <div class="wordmark">KIRO</div>
  </section>

  <section class="card card--back" aria-label="Card back">
    <div class="holder">
      <p class="holder__name">Dorian Pallister</p>
      <p class="holder__role">Manager</p>
    </div>

    <ul class="contacts">
      <li>
        <svg viewBox="0 0 12 12" aria-hidden="true"><rect x="3" y="1" width="6" height="10" rx="1"/><line x1="5.2" y1="9.2" x2="6.8" y2="9.2"/></svg>
        1 (212) 555-0143
      </li>
      <li>
        <svg viewBox="0 0 12 12" aria-hidden="true"><path d="M2 1.5h2.5l1 2.5-1.5 1a6 6 0 0 0 3 3l1-1.5 2.5 1v2.5A1 1 0 0 1 9.5 11 8.5 8.5 0 0 1 1 2.5 1 1 0 0 1 2 1.5z"/></svg>
        1 (212) 555-0178
      </li>
      <li>
        <svg viewBox="0 0 12 12" aria-hidden="true"><rect x="1" y="2.5" width="10" height="7"/><path d="M1 2.5l5 4 5-4"/></svg>
        dorian27@kiroharbour-mail.com
      </li>
      <li>
        <svg viewBox="0 0 12 12" aria-hidden="true"><path d="M6 11S2 7 2 4.5a4 4 0 0 1 8 0C10 7 6 11 6 11z"/><circle cx="6" cy="4.5" r="1.3"/></svg>
        482 Halden Ave, New York, NY 10160, USA
      </li>
    </ul>

    <div class="wordmark">KIRO</div>
  </section>
</main>
</body>
</html>
```